Owen Tasker Studios Business Card

Looking for a clear, modern, elegant, sharp business card that conveys a professional yet edgy image to my business as a wedding, portrait, and travel photographer. Would like something that looks vintage yet modern. Need a new business card to grow my business. We are growing the business for Wedding and Event Photography as well as fine art Photography. (Mostly Landscapes)
Updates

I’m looking through designs now but I have a new logo that i want using please.

New logo uploaded please redesign using that

PLEASE ALL DESIGNERS LOOK IN BRIEF FOR NEW LOGO

Target Market(s)

Brides, Grooms, Families with Kids, People looking for Fine Art Photography Artwork

Industry/Entity Type

Photographer

Contact Information for Business Card

Unsure

Font styles to use
Serif

Colors

Designer to choose colors to be used in the design.

Requirements
Must have
• My Website:
• http://taskerlens.examplefolio.net
• Phone:
• 323-481-5206
• Email:
• owentaskerlens@mailbox-example.net
Nice to have
• Would like a sort of shine on the printing finish.
• I like black I think it looks good on a business card.
• Can try working with my logo (png that I've attached)

```html
<!DOCTYPE html>
<html lang="en">
<head>
<meta charset="utf-8">
<title>Owen Tasker Studios – Business Card</title>
<link rel="stylesheet" href="https://fonts.googleapis.com/css2?family=Quicksand:wght@300;400;500&display=swap">
<style>
  :root {
    --canvas: #ececee;
    --card-black: #1c1c1c;
    --card-black-deep: #141414;
    --band-grey: #3a3a3a;
    --paper-white: #f7f7f7;
    --paper-shade: #e6e6e6;
    --accent-teal: #2fb3b3;
    --text-light: #e4e4e4;
    --text-muted: #bdbdbd;
    --text-dark: #2b2b2b;
  }
  * { box-sizing: border-box; margin: 0; padding: 0; }
  html, body {
    width: 1200px; height: 800px; overflow: hidden;
    background: var(--canvas);
    font-family: "Quicksand", sans-serif;
  }
  .stage { position: relative; width: 1200px; height: 800px; }

  .card {
    position: absolute; left: 390px; width: 420px; height: 240px;
    overflow: hidden;
  }
  .card--front {
    top: 130px;
    background: linear-gradient(160deg, var(--card-black) 0%, var(--card-black-deep) 100%);
  }
  .card--back { top: 430px; background: var(--paper-white); }

  .corner-marks { position: absolute; inset: 0; }

  .brand-dot {
    position: absolute; border-radius: 50%;
    background: var(--accent-teal);
  }
  .card--front .brand-dot { width: 74px; height: 74px; left: 173px; top: 47px; }

  .brand-name, .brand-sub {
    position: absolute; left: 0; width: 100%; text-align: center;
    font-weight: 300;
  }
  .brand-name { font-size: 22px; color: var(--text-light); letter-spacing: 0.5px; }
  .brand-sub { font-size: 15px; color: var(--text-muted); letter-spacing: 1px; }
  .card--front .brand-name { top: 128px; }
  .card--front .brand-sub { top: 161px; }

  .back-top {
    position: absolute; left: 0; top: 0; width: 100%; height: 113px;
    background: linear-gradient(180deg, var(--card-black) 0%, var(--card-black-deep) 100%);
  }
  .back-band {
    position: absolute; left: 0; top: 113px; width: 100%; height: 13px;
    background: var(--band-grey);
  }
  .back-paper {
    position: absolute; left: 0; top: 126px; width: 100%; height: 114px;
    background: linear-gradient(180deg, var(--paper-white) 0%, var(--paper-shade) 100%);
  }
  .card--back .brand-name { top: 28px; }
  .card--back .brand-sub { top: 61px; }
  .card--back .brand-dot { width: 60px; height: 60px; left: 180px; top: 96px; }

  .contact-list {
    position: absolute; left: 0; top: 160px; width: 100%;
    list-style: none; text-align: center;
    font-size: 11.5px; font-weight: 500; color: var(--text-dark);
  }
  .contact-list li { height: 23px; line-height: 18px; }
</style>
</head>
<body>
<main class="stage">
  <section class="card card--front" aria-label="Card front">
    <svg class="corner-marks" width="420" height="240" viewBox="0 0 420 240" aria-hidden="true">
      <g fill="none" stroke="#ffffff" stroke-width="1.5">
        <path d="M9 26 V10 H25"/>
        <path d="M395 10 H411 V26"/>
        <path d="M9 214 V230 H25"/>
        <path d="M395 230 H411 V214"/>
      </g>
    </svg>
    <span class="brand-dot" aria-hidden="true"></span>
    <h1 class="brand-name">Owen Tasker</h1>
    <p class="brand-sub">Studios</p>
  </section>

  <section class="card card--back" aria-label="Card back">
    <div class="back-top"></div>
    <div class="back-band"></div>
    <div class="back-paper"></div>
    <h2 class="brand-name">Owen Tasker</h2>
    <p class="brand-sub">Studios</p>
    <span class="brand-dot" aria-hidden="true"></span>
    <ul class="contact-list">
      <li>P: 323-481-5206</li>
      <li>E: owentaskerlens@mailbox-example.net</li>
      <li>W: http://taskerlens.examplefolio.net</li>
    </ul>
  </section>
</main>
</body>
</html>
```